Investor Services
Zielgruppe
Unsere Broschüre richtet sich an Investoren und Kapitalanleger, die Ihre Ferienwohnung nicht selbst nutzen und gut vermarktet wissen wollen. Die Broschüre soll für unser Unternehmen 'Sonnenklare Tage Ihre Urlaubsverwalter' als Akquisehilfsmittel genutzt werden. Sonnenklare Tage Ihre Urlaubsverwalter vermietet hochwertige Ferienwohnungen in Greetsiel und auf Ameland. Zielgruppe sind Endkunden, wie Familien mit und ohne Kinder, Paare, Paare mit und ohne Hund, Alleinreisende mit und ohne Hund - alle mittleren Alters.
Aufgabenstellung
Achtung Änderung: Ich habe den Eindruck, dass die von uns hochgeladene Version für den Umfang nur verwirrt und habe aus dem Grund jetzt die Datei gelöscht und die reinen Texte hochgeladen!
Wir lieben verschwenderische Gestaltung mit viel Freiraum. Die Texte sollen nicht auf wenige Seiten gequetscht werden. Ein quadratisches Format von 20*20 finden wir gut, ist aber keine feste Vorgabe. Auch können wir uns ein Format in 20*25 vorstellen, mal etwas, was anders ist aber auch keine feste Vorgabe. Wir fügen Ihnen die groben Texte, die in einem Ansichtslayout sind (bitte Typo und Gestaltung überhaupt nicht beachten, es ist nur eine Skizze, um eine Idee von Aufbau und Umfang zu bekommen) bei - mit den Texten ist es ggfs. einfacher, Design und Format zu entscheiden. Ich habe weiterhin ein paar Fotos hochgeladen, auch nur zur Ansicht, damit Sie wissen, was in etwa an Material da ist.
Gerne würden wir später im Druck die Broschüre veredeln - ggfs. mit einer Heißfolienprägung auf dem Titel, oder, wenn es das Design zulässt, auch im Inhalt.
Bitte beim Logo den Zusatz 'Ihre Fewovermieter' auswechseln gegen 'Investor Services'.

```html
<!DOCTYPE html>
<html lang="de">
<head>
<meta charset="utf-8">
<title>Sonnenklare Tage – Investor Services Broschüre</title>
<link href="https://fonts.googleapis.com/css2?family=Cormorant+Garamond:ital,wght@1,400;1,500&family=Open+Sans:wght@300;400&display=swap" rel="stylesheet">
<style>
  :root {
    --backdrop: #e9e9e9;
    --paper: #ffffff;
    --gutter-shade: rgba(0,0,0,0.06);
    --ink-heading: #3a3a3a;
    --ink-body: #8a8a8a;
    --ink-lead: #6e6e6e;
    --photo-sky: #8d9bb0;
    --photo-light: #d9c7a8;
    --photo-green: #5f8a3e;
    --photo-water: #45546a;
    --photo-hull: #2f3a40;
    --sign-tone: #e6e6e6;
  }
  * { box-sizing: border-box; margin: 0; padding: 0; }
  html, body { width: 1199px; height: 1200px; overflow: hidden; background: var(--backdrop); }
  body { position: relative; font-family: "Open Sans", Arial, sans-serif; }

  .spread {
    position: absolute;
    left: 120px;
    width: 960px;
    height: 480px;
    display: flex;
    box-shadow: 0 10px 30px rgba(0,0,0,0.10);
  }
  .spread--experience { top: 80px; }
  .spread--portrait { top: 640px; }

  .page { position: relative; width: 480px; height: 480px; background: var(--paper); }
  .page--left { background: linear-gradient(to right, var(--paper) 88%, #f4f4f4 100%); }
  .page--right { background: linear-gradient(to left, var(--paper) 88%, #f4f4f4 100%); }
  .spread::after {
    content: ""; position: absolute; left: 479px; top: 0; width: 2px; height: 100%;
    background: var(--gutter-shade);
  }

  .harbour-photo {
    position: absolute; left: 170px; top: 62px; width: 400px; height: 250px; z-index: 2;
    background: linear-gradient(to bottom,
      var(--photo-sky) 0%, #a9b2bf 28%, var(--photo-light) 40%,
      var(--photo-green) 46%, #7d8ea6 55%, var(--photo-water) 75%, var(--photo-hull) 100%);
  }

  .heading {
    font-family: "Cormorant Garamond", Georgia, serif;
    font-style: italic; font-weight: 500;
    color: var(--ink-heading);
    line-height: 1.05;
  }
  .lead {
    font-family: "Cormorant Garamond", Georgia, serif;
    font-style: italic; font-weight: 400;
    color: var(--ink-lead);
    font-size: 9.5px; line-height: 1.3;
  }
  .body-copy p {
    font-weight: 300; color: var(--ink-body);
    font-size: 7.6px; line-height: 1.55;
    margin-bottom: 8px;
  }

  .experience-text { position: absolute; left: 150px; top: 150px; width: 190px; }
  .experience-text .heading { font-size: 24px; margin-bottom: 6px; }
  .experience-text .lead { margin-bottom: 10px; }

  .portrait-title { position: absolute; left: 110px; top: 150px; width: 240px; text-align: center; }
  .portrait-title .heading { font-size: 22px; margin-bottom: 8px; }

  .portrait-columns { position: absolute; left: 70px; top: 80px; width: 370px; display: flex; gap: 30px; }
  .portrait-columns .column { width: 170px; }
  .portrait-columns .column--narrow { width: 150px; padding-top: 18px; }
  .signature { display: block; width: 80px; height: 16px; background: var(--sign-tone); margin-top: 4px; }
</style>
</head>
<body>

<section class="spread spread--experience">
  <div class="page page--left"></div>
  <div class="page page--right">
    <div class="experience-text">
      <h2 class="heading">Erfahrung</h2>
      <p class="lead">Seit vielen Jahren betreuen wir hochwertige Ferienwohnungen an der Küste und kennen die Wünsche anspruchsvoller Gäste genau.</p>
      <div class="body-copy">
        <p>Heute sind wir Ihre erste Adresse, wenn es um die Vermietung von Ferienwohnungen in Greetsiel und auf Ameland geht. Mit Erfahrung, Sorgfalt und Herz sorgen wir dafür, dass sich Gäste wohlfühlen und gerne wiederkommen.</p>
        <p>Wir bieten Ihnen nun unsere Investor Services an – wir sind selbst Eigentümer und wissen, was Ihnen am Herzen liegt.</p>
      </div>
    </div>
  </div>
  <div class="harbour-photo" role="img" aria-label="Foto: Krabbenkutter im Hafen von Greetsiel bei Abendhimmel, Spiegelung im Wasser"></div>
</section>

<section class="spread spread--portrait">
  <div class="page page--left">
    <div class="portrait-title">
      <h2 class="heading">Sonnenklare Tage<br>ein Portrait</h2>
      <p class="lead">Sonnenklare Tage steht seit Jahren für Ferienwohnungen, die gepflegt und stilvoll eingerichtet sind, mit persönlichem Service für jeden Gast.</p>
    </div>
  </div>
  <div class="page page--right">
    <div class="portrait-columns body-copy">
      <div class="column">
        <p>Wir glauben an die Liebe zum Detail. Unsere Gäste sollen sich vom ersten Moment an zu Hause fühlen, ob bei einem Wochenende am Meer oder in den langen Sommerferien mit der ganzen Familie.</p>
        <p>Alles begann mit unserer eigenen Ferienwohnung. Schnell kamen weitere Wohnungen hinzu, und mit ihnen die Freude an der Arbeit mit Eigentümern und Gästen.</p>
        <p>Heute betreuen wir zahlreiche Objekte an der Nordseeküste. Unser Team kümmert sich um Buchung, Reinigung, Pflege und die persönliche Begrüßung vor Ort.</p>
        <p>Unsere Gäste schätzen die Ruhe, die Weite und den Charme der Region. Viele von ihnen kommen Jahr für Jahr wieder zu uns.</p>
      </div>
      <div class="column column--narrow">
        <p>Die Liebe zu diesen Orten wurde größer und wir möchten sie mit Ihnen teilen. Mit unseren Investor Services bieten wir Ihnen einen verlässlichen Partner.</p>
        <p>Wir freuen uns über jede Anfrage und nehmen uns Zeit für ein persönliches Gespräch.</p>
        <p>Ein Partner, der mitdenkt, transparent arbeitet und Ihre Wohnung so behandelt, als wäre es die eigene. Das ist unser Versprechen an Sie.</p>
        <p>Gemeinsam schaffen wir unvergessliche Ferien.</p>
        <p>Wir freuen uns auf Sie.</p>
        <p>Herzlich,<span class="signature" role="img" aria-label="Handschriftliche Unterschrift"></span></p>
      </div>
    </div>
  </div>
</section>

</body>
</html>
```